Package Design for Plant-based Dumplings

We need a CPG Package design for a new product we're launching. I included example (front and back) of what a typical information food package has, so you can use it as reference.

Target Market(s)

Consumers that are seeking non-meat items. Environment concerned consumers.

Colors

Designer to choose colors to be used in the design.

Requirements
Must have
• Modern and clean looking design.
Nice to have
• might have multiple flavors, so make design where it could be have multiple variations.

```html
<!DOCTYPE html>
<html lang="en">
<head>
<meta charset="utf-8">
<title>MaeSun Foods – Plant-Based Dumplings Package</title>
<link rel="stylesheet" href="https://fonts.googleapis.com/css2?family=Inter:wght@400;600;700;800&family=Arimo:wght@400;700&display=swap">
<style>
:root{
  --orange:#f54a16;
  --red:#f3200f;
  --band-dark:rgba(190,40,20,.55);
  --ink:#111;
  --slate-1:#3b3d40;
  --slate-2:#232427;
  --white:#fff;
}
*{margin:0;padding:0;box-sizing:border-box}
html,body{width:1200px;height:912px;overflow:hidden;background:var(--white)}
body{position:relative;font-family:"Inter",sans-serif;color:var(--ink)}

/* Panels */
.panel{position:absolute;top:69px;height:770px;border:1px solid #555;overflow:hidden}
.panel-front{left:43px;width:552px}
.panel-back{left:607px;width:549px;background:var(--white)}

/* Front */
.hero-photo{position:absolute;inset:0;
  background:radial-gradient(circle at 48% 58%,#5a4a38 0,#2c2622 24%,transparent 44%),
             radial-gradient(circle at 30% 20%,var(--slate-1),var(--slate-2) 75%)}
.brand-name{position:absolute;font-family:"Inter",sans-serif;font-weight:800;line-height:1;white-space:nowrap}
.front-brand{left:140px;top:60px;width:320px;text-align:center;color:var(--white);font-size:44px}
.back-brand{left:0;top:62px;width:549px;text-align:center;color:var(--ink);font-size:52px}

.title-shadow{position:absolute;left:0;top:160px;width:462px;height:70px;background:var(--band-dark);border-radius:0 6px 6px 0}
.title-band{position:absolute;left:0;top:182px;width:403px;height:84px;background:var(--red);border-radius:0 6px 6px 0;color:var(--white);padding:10px 0 0 6px}
.title-band h1{font-size:33px;font-weight:700;line-height:1.05;letter-spacing:.2px;white-space:nowrap}
.title-band p{font-size:19px;font-weight:600;margin:4px 0 0 6px;white-space:nowrap}

.front-footer{position:absolute;left:0;top:0;width:552px;height:770px}
.claims{position:absolute;right:16px;top:586px;text-align:right;color:var(--white);font-size:23.5px;font-weight:600;line-height:23px}
.net-weight{position:absolute;left:11px;top:700px;color:var(--orange);font-size:21px;font-weight:600;line-height:28px}

/* Back */
.story{position:absolute;left:21px;top:150px;width:505px;font-size:14.4px;font-weight:600;line-height:22.9px}

.ingredients{position:absolute;left:21px;top:323px;width:323px;font-size:7px;font-weight:700;line-height:15px;text-transform:uppercase;letter-spacing:.1px}
.ingredients p+p{margin-top:15px}
.heating{position:absolute;left:21px;top:566px;width:360px;font-size:7px;font-weight:700;line-height:15px}

.nutrition{position:absolute;left:358px;top:316px;width:157px;height:281px;border:1px solid #222;padding:3px 4px;font-family:"Arimo",sans-serif;font-size:6.4px;line-height:1.1;overflow:hidden}
.nutrition h2{font-size:17.5px;font-weight:700;line-height:1;border-bottom:1px solid #222;padding-bottom:2px}
.nf-servings{padding:2px 0 2px;border-bottom:5px solid #111}
.nf-cal{display:flex;justify-content:space-between;align-items:flex-end;border-bottom:3px solid #111;padding:3px 0 1px}
.nf-cal b{font-size:13px}
.nf-cal strong{font-size:20px;line-height:1}
.row{display:flex;justify-content:space-between;border-bottom:.5px solid #777;padding:1.4px 0}
.row.thick{border-bottom:5px solid #111}
.dv{text-align:right;font-weight:700;border-bottom:.5px solid #777;padding:1px 0}
.nf-note{font-size:4.6px;line-height:1.2;margin-top:3px;border-top:3px solid #111;padding-top:2px}

.barcode-label{position:absolute;left:415px;top:611px;font-size:12px;font-weight:700}
.barcode-box{position:absolute;left:377px;top:626px;width:139px;height:72px;border:1px solid #222;display:flex;align-items:center;justify-content:center;font-size:12px;font-weight:600}
.maker{position:absolute;right:33px;top:719px;text-align:right;font-size:7px;font-weight:700;line-height:15px}
</style>
</head>
<body>

<section class="panel panel-front" aria-label="Package front">
  <div class="hero-photo" role="img" aria-label="Pan-fried plant-based dumplings with sesame seeds in a cast-iron skillet on dark slate, with wooden chopsticks"></div>

  <div class="brand-name front-brand">MaeSun<br>Foods</div>

  <div class="title-shadow"></div>
  <div class="title-band">
    <h1>Plant-Based Dumplings</h1>
    <p>Using Plant-based Meat and Vegetables</p>
  </div>

  <svg class="front-footer" viewBox="0 0 552 770" aria-hidden="true">
    <rect x="0" y="686" width="552" height="84" fill="#fff"/>
    <path d="M552 541 C455 556 385 620 322 690 C270 745 220 764 155 770 L552 770 Z" fill="#f54a16"/>
  </svg>

  <div class="claims">Vegan<br>Ready in Minutes<br>No Soy<br>20g of Protein</div>
  <div class="net-weight">Net Wt. 2 LBs (32oz)<br>Keep Frozen</div>
</section>

<section class="panel panel-back" aria-label="Package back">
  <div class="brand-name back-brand">MaeSun Foods</div>

  <p class="story">The brand name MaeSun Foods was inspired from a lady named Mae Sun that started a food business in S. Korea during the 1950s. Mae's family immigrated to the U.S. in late 1990s and the Sun family began making dumplings out-of-their home kitchen and sold into local markets. Business grew and the family eventually built a state-of-the-art USDA food factory in 2003. Dumplings made at MaeSun's factory is now available throughout retailers in US and Canada.</p>

  <div class="ingredients">
    <p>Ingredient List<br>Filling: Plant-based meat(water, pea protein isolate,canola and sunflower oil, rice flour, spice, tomato powder,contains 0.5% or less: yeast extract, sugar, potassium chloride,tapioca maltodextrin, citric acid, salt, acacia gum, onion extract,natural flavor, garlic extract ), cabbage, onion, sweet potato noodle(water, sweet potato starch), green onion, seasoning(onion powder, grilled flavor, sugar, garlic dehydrated, spice,natural flavor, yeast extract), carrot, water, starch (cornstarch,modified starch), sesame oil, canola oil, garlic.</p>
    <p>Dough:wheat flour enriched([niacin, reduced iron, thiamine mononitrate, riboflavin, folic acid] malted barley flour),water, conditioner(tapioca starch, salt, dextrose, potassium chloride, monoglycerides, modified cellulose gum, xanthan gum),canola oil.</p>
    <p style="text-transform:none">Allergens: Wheat</p>
  </div>

  <div class="heating">
    <p>Heating Instructions</p>
    <p>Steam:</p>
    <p>1. Remove frozen dumplings from the package and place them in a steamer over boiling water.</p>
    <p>2. Cover the steamer approximately 8-10 minutes or until cooked thoroughly.</p>
    <p>Pan Fry:</p>
    <p>1. Heat 2 teaspoons of oil in frying pan. Carefully place thawed dumplings into heated pan.</p>
    <p>2. Heat approximately 3-4 minutes or until golden brown.</p>
    <p>Microwave:</p>
    <p>1. Place frozen dumplings on microwave-safe dish.</p>
    <p>2. Cover with damp paper towel and heat on high for 2 to 3 minutes or until hot.</p>
  </div>

  <div class="nutrition">
    <h2>Nutrition Facts</h2>
    <div class="nf-servings">
      <div style="font-size:8px">about 8 servings per container</div>
      <div class="row" style="border:0;padding:0;font-weight:700;font-size:8px"><span>Servings Size</span><span>3 pieces (90g)</span></div>
    </div>
    <div class="nf-cal"><div><div style="font-size:5px;font-weight:700">Amount per serving</div><b>Calories</b></div><strong>180</strong></div>
    <div class="dv">% Daily Value</div>
    <div class="row"><span><b>Total Fat</b> 8g</span><b>10%</b></div>
    <div class="row"><span>Saturdated Fat 2.5g</span><b>13%</b></div>
    <div class="row"><span>Trans &nbsp; Fat 0g</span><span></span></div>
    <div class="row"><span><b>Cholesterol</b> 15mg</span><b>5%</b></div>
    <div class="row"><span><b>Sodium</b> 410mg</span><b>18%</b></div>
    <div class="row"><span><b>Total Carbohydrate</b> 19g</span><b>7%</b></div>
    <div class="row"><span>Dietary Fiber 1g</span><b>4%</b></div>
    <div class="row"><span>Total Sugars 2g</span><span></span></div>
    <div class="row"><span>Includes 1g Added Sugars</span><b>2%</b></div>
    <div class="row thick"><span><b>Protein</b> 8g</span><span></span></div>
    <div class="row"><span>Vitamin D &nbsp;0mcg</span><span>0%</span></div>
    <div class="row"><span>Calcium 30mg</span><span>2%</span></div>
    <div class="row"><span>Iron 1.2mg</span><span>6%</span></div>
    <div class="row"><span>Potassium 176mg</span><span>4%</span></div>
    <p class="nf-note">* The % Daily Value tells you how much a nutrient in a serving of food contributes to a daily diet. 2000 calories a day is used for general nutrition advise.</p>
  </div>

  <div class="barcode-label">Barcode:</div>
  <div class="barcode-box">place-holder for now</div>

  <div class="maker">Manufactured For:<br>Northgate Provisions<br>Riverside, CA 92501</div>
</section>

</body>
</html>
```